Fun and Flexible Word Template Design for Classroom Learning Resources

We're a global arts and education nonprofit based in New York. We're looking for a 2-page Word template design for our new collection of Learning Resources.
Page 1 of the template should include:
1. Lanternfold 7 logo (attached)
2. Resource title
3. Author photo
4. Author bio
5. Resource text
6. Sub-title text
7. Colored call-out box
Page 2 of the template should include:
2. Resource Title (in a smaller font)
3. Resource text
4. Sub-title text
5. Colored call-out box
The design must also adhere to our current brand guidelines: https://stylevault.example/lanternfold-7
We've attached a very basic mock-up that includes the elements listed above. However, we encourage you to be more playful and/or creative with your design.
Our goal is to create a template that is flexible enough to accomodate a variety of resources (samples of 3 different resources are attached), that is also visually appealing enough to attract and hold the attention of busy educators.
Target Market(s)
Educators - Middle School, High School & College
Look and feel

```html
<!DOCTYPE html>
<html lang="en">
<head>
<meta charset="utf-8">
<title>Lanternfold 7 – Learning Resource Template</title>
<link href="https://fonts.googleapis.com/css2?family=Bebas+Neue&family=Montserrat:wght@400;500;600;700&display=swap" rel="stylesheet">
<style>
  :root{
    --purple-deep:#3d1a78;
    --purple:#4f2391;
    --purple-light:#6c3ca8;
    --purple-text:#5a2a9c;
    --ink:#2a2233;
    --ink-dark:#16122b;
    --paper:#ffffff;
    --paper-shade:#e6e5ea;
    --stage:#e9e8ee;
  }
  *{box-sizing:border-box;margin:0;padding:0}
  html,body{width:1050px;height:1200px;overflow:hidden}
  body{background:var(--stage);font-family:"Montserrat",Arial,sans-serif;color:var(--ink);position:relative}

  .page{position:absolute;top:246px;width:500px;height:708px;overflow:hidden;
    background:linear-gradient(180deg,var(--paper) 0%,#f6f6f8 55%,var(--paper-shade) 100%);
    box-shadow:0 4px 18px rgba(20,10,40,.18)}
  .page--one{left:17px}
  .page--two{left:533px}
  .page-shapes{position:absolute;inset:0;width:500px;height:708px}
  .page-footer-band{position:absolute;left:0;right:0;bottom:0;height:6px;background:var(--purple-light)}

  .masthead{position:absolute;top:0;left:0;width:500px;height:61px;
    background:linear-gradient(180deg,#fff 0%,#e4e3e8 100%);
    display:flex;align-items:center;justify-content:center;gap:10px}
  .masthead-dot{width:45px;height:45px;border-radius:50%;background:var(--purple)}
  .masthead-name{font-weight:600;font-size:19px;letter-spacing:.8px;color:var(--purple);text-transform:uppercase}

  .block{position:absolute}
  .body-text{font-size:9.3px;line-height:11.7px;font-weight:400}
  .body-text p+p{margin-top:11.7px}
  .justify{text-align:justify}
  .on-purple{color:#fff}

  .resource-title{font-family:"Bebas Neue","Oswald",sans-serif;font-size:68px;line-height:60px;color:#fff;letter-spacing:.5px;white-space:nowrap}
  .resource-title .title-mark{background:var(--ink-dark);padding:0 2px}
  .resource-subtitle{font-weight:700;font-size:23px;line-height:26px;color:#fff;letter-spacing:.3px}
  .author-bio{font-weight:700;font-size:11.2px;line-height:15.3px;color:#fff}

  .section-label{font-weight:700;font-size:13px;letter-spacing:.3px;color:var(--purple-text);text-transform:uppercase}
  .section-label--white{color:#fff;font-weight:600}
  .subheader-kicker{font-weight:600;font-size:9.6px;letter-spacing:.3px;color:var(--ink);text-transform:uppercase}
  .subheader-title{font-weight:600;font-size:15px;line-height:19px;color:var(--purple-text);text-transform:uppercase;white-space:nowrap}

  .author-photo{position:absolute;left:330px;top:150px;width:134px;height:134px;border-radius:50%;overflow:hidden;
    background:radial-gradient(circle at 50% 40%,#b9b9b9 0%,#6e6e6e 55%,#2e2e2e 100%)}
  .author-photo-tag{position:absolute;left:0;right:0;bottom:0;height:27px;background:var(--purple);
    font-family:"Bebas Neue",sans-serif;font-size:15px;line-height:24px;color:#fff;text-align:center;letter-spacing:.4px}

  .cont-kicker{font-weight:600;font-size:11.4px;color:#fff;letter-spacing:.3px;text-transform:uppercase}
  .cont-title{font-weight:600;font-size:18.6px;color:#fff;letter-spacing:.3px;text-transform:uppercase;white-space:nowrap}
</style>
</head>
<body>

<section class="page page--one" aria-label="Resource page one">
  <svg class="page-shapes" viewBox="0 0 500 708" aria-hidden="true">
    <defs>
      <linearGradient id="heroFill" x1="0" y1="0" x2="1" y2="1">
        <stop offset="0" stop-color="#5b2b9a"/>
        <stop offset="1" stop-color="#3a1873"/>
      </linearGradient>
      <linearGradient id="calloutFill" x1="0" y1="0" x2="0" y2="1">
        <stop offset="0" stop-color="#6a3aa3"/>
        <stop offset="1" stop-color="#3f1b7b"/>
      </linearGradient>
    </defs>
    <path d="M0 61 H500 V262 L410 262 C372 262 362 178 322 190 C288 200 278 290 228 288 C188 287 168 266 120 270 C70 275 40 278 0 274 Z" fill="url(#heroFill)"/>
    <circle cx="397" cy="217" r="79" fill="none" stroke="#ffffff" stroke-opacity=".7" stroke-width="1"/>
    <circle cx="86" cy="577" r="152" fill="url(#calloutFill)"/>
  </svg>

  <header class="masthead">
    <span class="masthead-dot"></span>
    <span class="masthead-name">Lanternfold 7</span>
  </header>

  <h1 class="block resource-title" style="left:26px;top:88px"><span class="title-mark">RESOURCE</span> TITLE</h1>
  <h2 class="block resource-subtitle" style="left:26px;top:156px">LOREM IPSUM DOLOR</h2>
  <p class="block author-bio" style="left:26px;top:196px;width:280px">Lorem ipsum dolor sit amet Lorem ipsum dolor sit amet Lorem ipsum dolor sit amet Lorem ipsum dolor sit amet Lorem ipsum dolor sit amet Lorem ipsum dolor sit amet</p>

  <div class="author-photo" role="img" aria-label="Author portrait photo">
    <span class="author-photo-tag">WRITER PHOTO</span>
  </div>

  <h3 class="block section-label" style="left:31px;top:300px">RESOURCE TEXT</h3>
  <div class="block body-text justify" style="left:31px;top:320px;width:439px">
    <p>Lorem ipsum dolor sit amet, consectetur adipiscing elit. Morbi ut libero mattis, pellentesque urna eu, iaculis lorem. Interdum et malesuada fames ac ante ipsum primis in faucibus. Duis pellen- tesque orci consectetur sapien vulputate imperdiet. Aliquam erat volutpat.</p>
    <p>Integer tristique erat lorem, sed posuere enim rhoncus sed. Fusce ut venenatis nulla, sed elementum arcu. Maecenas eu- ismod mauris euismod augue posuere venenatis. Duis id porta ante integer.</p>
  </div>

  <div class="block" style="left:252px;top:421px">
    <p class="subheader-kicker">SUB-HEADER TEXT -</p>
    <h3 class="subheader-title">LOREM IPSUM DOLOR SIT</h3>
  </div>
  <div class="block body-text" style="left:252px;top:462px;width:215px">
    <p>Lorem ipsum dolor sit amet, consectetur adipiscing elit. Morbi ut libero mattis, pellentesque urna eu, iaculis lorem. Interdum et malesuada fames ac ante ipsum primis in faucibus. Duis pellen- tesque orci consectetur sapien vulputate imperdiet. Aliquam erat volutpat. Integer tristique erat lorem, sed posuere enim rhoncus sed.</p>
    <p>Fusce ut venenatis nulla, sed elementum arcu. Maecenas eu- ismod mauris euismod augue posuere venenatis. Duis id porta ante integer.</p>
    <p>Fusce ut venenatis nulla, sed elementum arcu. Maecenas eu- ismod mauris euismod augue posuere venenatis. Duis id porta ante integer. Fusce ut venenatis nulla, sed elementum arcu.</p>
  </div>

  <div class="block body-text on-purple" style="left:31px;top:484px;width:160px">
    <p>Lorem ipsum dolor sit amet, consectetur adipiscing elit. Morbi ut libero mattis, pellentesque urna eu, iaculis lorem. Interdum et malesuada fames ac ante ipsum primis in faucibus. Duis pellen- tesque orci consectetur sapien vulputate imperdiet. Aliquam erat volutpat.</p>
    <p>Integer tristique erat lorem, sed posuere enim rhoncus sed. Fusce ut venenatis nulla, sed elementum arcu. Maecenas eu- ismod mauris euismod augue posuere venenatis. Duis id porta ante integer.</p>
  </div>

  <div class="page-footer-band"></div>
</section>

<section class="page page--two" aria-label="Resource page two">
  <svg class="page-shapes" viewBox="0 0 500 708" aria-hidden="true">
    <defs>
      <linearGradient id="contFill" x1="0" y1="0" x2="1" y2="1">
        <stop offset="0" stop-color="#4a2089"/>
        <stop offset=".6" stop-color="#5a2a98"/>
        <stop offset="1" stop-color="#3c1a76"/>
      </linearGradient>
    </defs>
    <circle cx="160" cy="126" r="335" fill="none" stroke="#ffffff" stroke-width="1.2" stroke-opacity=".9"/>
    <circle cx="160" cy="126" r="327" fill="url(#contFill)"/>
  </svg>

  <p class="block cont-kicker" style="left:31px;top:24px">RESOURCE TITLE TEXT</p>
  <h2 class="block cont-title" style="left:31px;top:42px">LOREM IPSUM DOLOR SIT (CONT’D)</h2>
  <h3 class="block section-label section-label--white" style="left:31px;top:84px">RESOURCE TEXT</h3>

  <div class="block body-text justify on-purple" style="left:31px;top:105px;width:416px">
    <p>Lorem ipsum dolor sit amet, consectetur adipiscing elit. Morbi ut libero mattis, pellentesque urna eu, iaculis lorem. Interdum et malesuada fames ac ante ipsum primis in faucibus. Duis pellen- tesque orci consectetur sapien vulputate imperdiet. Aliquam erat volutpat. Integer tristique erat lorem, sed posuere enim rhoncus sed. Fusce ut venenatis nulla, sed elementum arcu. Maecenas eu- ismod mauris euismod augue posuere venenatis.</p>
    <p>Lorem ipsum dolor sit amet, consectetur adipiscing elit. Morbi ut libero mattis, pellentesque urna eu, iaculis lorem. Interdum et malesuada fames ac ante ipsum primis in faucibus. Duis pellen- tesque orci consectetur sapien vulputate imperdiet. Aliquam erat volutpat. Integer tristique erat lorem, sed posuere enim rhoncus sed. Fusce ut venenatis nulla, sed elementum arcu. Maecenas eu- ismod mauris euismod augue posuere venenatis.</p>
  </div>
  <div class="block body-text on-purple" style="left:31px;top:268px;width:375px">
    <p>Lorem ipsum dolor sit amet, consectetur adipiscing elit. Morbi ut libero mattis, pellentesque urna eu, iaculis lorem. Interdum et malesuada fames ac ante ipsum primis in faucibus. Duis pellen- tesque orci consectetur sapien vulputate imperdiet. Aliquam erat volutpat. Integer tristique erat lorem, sed posuere enim rhoncus sed. Fusce ut venenatis nulla, sed elementum arcu. Maecenas eu- ismod mauris euismod augue posuere venenatis.</p>
  </div>
  <div class="block body-text on-purple" style="left:31px;top:350px;width:330px">
    <p>Lorem ipsum dolor sit amet, consectetur adipiscing elit. Morbi ut libero mattis, pellentesque urna eu, iaculis lorem. Interdum et malesuada fames ac ante ipsum primis in faucibus. Duis pellen- tesque orci consectetur sapien vulputate imperdiet.</p>
  </div>

  <div class="block body-text" style="left:31px;top:486px;width:186px">
    <p>Lorem ipsum dolor sit amet, consectetur adipiscing elit. Morbi ut libero mattis, pellentesque urna eu, iaculis lorem. Interdum et malesuada fames ac ante ipsum primis in faucibus. Duis pellen- tesque orci consectetur sapien vulputate imperdiet. Aliquam erat volutpat.</p>
    <p>Integer tristique erat lorem, sed posuere enim rhoncus sed. Fusce ut venenatis nulla, sed elementum arcu. Maecenas eu- ismod mauris euismod augue posuere venenatis. Duis id porta ante integer.</p>
  </div>

  <div class="block" style="left:261px;top:464px">
    <p class="subheader-kicker">SUB-HEADER TEXT -</p>
    <h3 class="subheader-title">LOREM IPSUM DOLOR SIT</h3>
  </div>
  <div class="block body-text justify" style="left:261px;top:502px;width:207px">
    <p>Lorem ipsum dolor sit amet, consectetur adipiscing elit. Morbi ut libero mattis, pellentesque urna eu, iaculis lorem. Interdum et malesuada fames ac ante ipsum primis in faucibus.</p>
    <p>Duis pellen- tesque orci consectetur sapien vulputate imperdiet.</p>
    <p>Aliquam erat volutpat. Integer tristique erat lorem, sed posuere enim rhoncus sed. Fusce ut venenatis nulla, sed elementum arcu. Maecenas eu- ismod mauris euismod augue posuere venenatis. Duis id porta ante integer.</p>
  </div>

  <div class="page-footer-band"></div>
</section>

</body>
</html>
```